Political Candidate Newspaper Advertisement

I would like a newspaper ad for my campaign for election to City Council. The banner ad is 10 cm high x 26.2 cm wide. The banner will contain a photo and the following text (or words to similar effect):
VOTE
DENNIS HALE
COMO BEACH
For a
SAFE
CARING
CONNECTED
COMMUNITY
Lifetime commitment to local clubs, charities and international aid
Local business owner
Founder of Open-Gate Week
Councillor, Mediator, B.Sc., MBA
The Councillor you know and can call for help
Respects our heritage and our future
Listens to the wisdom and needs of older residents
Promotes more young people
Protects our South Perth environment
Authorised by Dennis Hale 5/348 Kelby Rd, Como. 9317 2864
I use MS Publisher and PhotoShop so I'd like the product to be in a form I can use. After ther banner ad is done, and if it is good, I wish to pay the designer to use the same theme to produce another newspaper ad, a brochure and a poster.
My simple version is attached. A photo is also attached.
I'm hoping you do better.
18-80 years old
Business
- simple fonts
- A TICK somewhere around the word Vote would be good.
Mention of www.fairlandward.notepage.net if possible, perhaps at the bottom of the page, along with the Authorised by ... text.

```html
<!DOCTYPE html>
<html lang="en">
<head>
<meta charset="utf-8">
<title>Vote Dennis Hale – Como Beach</title>
<link rel="stylesheet" href="https://fonts.googleapis.com/css2?family=Arimo:ital,wght@0,400;0,700;1,700&family=Tinos:wght@700&display=swap">
<style>
  :root {
    --cream: #fcfcc6;
    --red: #e3161b;
    --blue: #2b3fd9;
    --green: #5ad21a;
    --green-dark: #3a9a10;
    --ink: #111111;
    --white: #ffffff;
  }
  * { box-sizing: border-box; margin: 0; padding: 0; }
  html, body { width: 1200px; height: 458px; overflow: hidden; background: var(--cream); }
  .banner {
    position: relative; width: 1200px; height: 458px; overflow: hidden;
    background: var(--cream); font-family: "Arimo", Arial, sans-serif;
  }
  .candidate-photo {
    position: absolute; left: 22px; top: 25px; width: 270px; height: 400px;
    border: 2px solid var(--red);
    background: linear-gradient(180deg, #f4f2ef 0%, #e9dfd6 35%, #3a3a3c 60%, #1e1e20 100%);
    box-shadow: 4px 4px 6px rgba(0,0,0,0.35);
  }
  .headline {
    position: absolute; left: 298px; top: 6px; white-space: nowrap;
    font-family: "Tinos", "Times New Roman", serif; font-weight: 700;
    font-size: 57px; line-height: 1;
    color: var(--red); transform: scaleX(0.668); transform-origin: left top;
  }
  .qualities { position: absolute; left: 313px; top: 96px; color: var(--blue); }
  .qualities-intro { font-size: 21px; line-height: 24px; margin-bottom: 28px; }
  .quality-list { list-style: none; }
  .quality-list li {
    position: relative; padding-left: 35px; font-size: 18.5px; line-height: 24px;
    width: 355px; margin-bottom: 18px;
  }
  .quality-list li svg { position: absolute; left: 0; top: 2px; width: 30px; height: 28px; }
  .vote-block { position: absolute; left: 790px; top: 82px; width: 280px; text-align: center; }
  .vote-word, .vote-name {
    color: var(--red); font-weight: 700; font-style: italic; line-height: 1;
  }
  .vote-word { font-size: 34px; letter-spacing: 1px; }
  .vote-name { font-size: 39px; margin-top: 8px; white-space: nowrap; }
  .ward { color: var(--blue); font-weight: 700; font-size: 20px; margin-top: 10px; }
  .pledge { color: var(--red); font-size: 18px; line-height: 30px; margin-top: 4px; }
  .pledge .intro { font-size: 17px; }
  .vote-tick { position: absolute; left: 1060px; top: 72px; width: 108px; height: 110px; }
  .credentials {
    position: absolute; left: 690px; top: 306px; width: 510px; height: 134px;
    background: var(--white); padding: 12px 0 0 18px; color: var(--ink);
    font-size: 13.5px; line-height: 22px;
  }
  .credentials p { line-height: 17px; }
  .credentials ul { list-style: none; margin-top: 2px; }
  .stamp {
    position: absolute; left: 1044px; top: 380px; padding: 3px 8px;
    border: 3px solid var(--red); border-radius: 4px; color: var(--red);
    font-weight: 700; font-size: 30px; line-height: 1; letter-spacing: 1px;
    white-space: nowrap;
    transform: rotate(-16deg); transform-origin: center; background: var(--white);
  }
</style>
</head>
<body>
<main class="banner">
  <div class="candidate-photo" role="img" aria-label="Portrait photo of candidate Dennis Hale in a dark suit and patterned tie"></div>

  <h1 class="headline">I DON’T PROMISE IT, TOGETHER WE PROVE IT.</h1>

  <section class="qualities">
    <p class="qualities-intro">Looking for The Councillor who :</p>
    <ul class="quality-list">
      <li><svg viewBox="0 0 30 28"><path d="M2 15 L11 25 L28 2 L11 18 Z" fill="var(--green)"/></svg>You know and can call for help ?</li>
      <li><svg viewBox="0 0 30 28"><path d="M2 15 L11 25 L28 2 L11 18 Z" fill="var(--green)"/></svg>Respects our heritage and our future ?</li>
      <li><svg viewBox="0 0 30 28"><path d="M2 15 L11 25 L28 2 L11 18 Z" fill="var(--green)"/></svg>Listens to the wisdom and needs of older residents ?</li>
      <li><svg viewBox="0 0 30 28"><path d="M2 15 L11 25 L28 2 L11 18 Z" fill="var(--green)"/></svg>Promotes more young people?</li>
      <li><svg viewBox="0 0 30 28"><path d="M2 15 L11 25 L28 2 L11 18 Z" fill="var(--green)"/></svg>Protects our South Perth environment ?</li>
    </ul>
  </section>

  <section class="vote-block">
    <p class="vote-word">VOTE</p>
    <p class="vote-name">DENNIS HALE</p>
    <p class="ward">COMO BEACH</p>
    <p class="pledge"><span class="intro">For a</span><br>SAFE - CARING and<br>CONNECTED COMMUNITY</p>
  </section>

  <svg class="vote-tick" viewBox="0 0 108 110" aria-hidden="true">
    <path d="M4 62 L38 104 L104 4 L98 2 L38 80 L18 52 Z" fill="var(--green)" stroke="var(--green-dark)" stroke-width="2"/>
  </svg>

  <section class="credentials">
    <p>Authorised by :<br>Dennis Hale 5/348 Kelby Rd, Como. 9317 2864</p>
    <ul>
      <li>&gt; Lifetime commitment to local clubs, charities and international aid</li>
      <li>&gt; Local business owner</li>
      <li>&gt; Founder of Open-Gate Week</li>
      <li>&gt; Councillor, Mediator, B.Sc., MBA</li>
    </ul>
  </section>

  <div class="stamp">I VOTED</div>
</main>
</body>
</html>
```